Tranquilly Balanced Restoration

We want to design a business card that is modern and appealing for an innovative psychedelic telemedicine company that provides at-home ketamine-assisted therapy along with wellness, longevity, and anti-aging medicines. We want to use our deep purple and white plus other colors you can find on our website. We don't have any strict brand guidelines yet so feel free to get creative. We want a very professional, but technology first modern design that will instill trust, peace, calm, but also be attractive to investors in the healthcare and SaaS space.

```html
<!DOCTYPE html>
<html lang="en">
<head>
<meta charset="utf-8">
<title>Tranquilly — Business Card</title>
<link rel="stylesheet" href="https://fonts.googleapis.com/css2?family=Open+Sans:wght@400;600;700&display=swap">
<style>
  :root {
    --bg: #e3e3e3;
    --purple: #6f55a3;
    --purple-deep: #6a4ea6;
    --orchid: #a35aa7;
    --ink: #222222;
    --white: #ffffff;
    --rule: #d9d4e2;
  }
  * { box-sizing: border-box; margin: 0; padding: 0; }
  html, body {
    width: 1200px; height: 871px; overflow: hidden;
    background: var(--bg);
    font-family: "Open Sans", Arial, sans-serif;
  }
  .sheet {
    width: 1200px; height: 871px;
    display: flex; flex-direction: column;
    align-items: center; justify-content: center; gap: 60px;
  }
  .card {
    width: 520px; height: 297px;
    box-shadow: 0 8px 22px rgba(0,0,0,0.12);
    position: relative;
  }
  .card--front {
    background: var(--white);
    display: flex; align-items: center;
  }
  .brand {
    width: 200px; display: flex; flex-direction: column; align-items: center; gap: 12px;
  }
  .brand__dot {
    width: 44px; height: 44px; border-radius: 50%; background: var(--purple);
  }
  .brand__name {
    font-size: 26px; font-weight: 400; color: var(--orchid); letter-spacing: 0.5px;
  }
  .divider {
    width: 1px; height: 130px; background: var(--rule);
  }
  .details {
    padding-left: 26px; color: var(--ink); font-size: 10.5px; line-height: 1.5;
  }
  .details__name {
    font-size: 16px; font-weight: 700; color: var(--purple-deep); line-height: 1.2;
  }
  .details__role { font-size: 12.5px; margin-bottom: 10px; }
  .details__address { margin-bottom: 10px; }
  .contact { list-style: none; }
  .contact__item { display: flex; align-items: center; gap: 8px; margin-bottom: 2px; }
  .contact__icon {
    width: 14px; height: 14px; border-radius: 50%; background: var(--orchid);
    display: flex; align-items: center; justify-content: center; flex: none;
  }
  .card--back {
    background: var(--purple);
    display: flex; flex-direction: column; align-items: center; justify-content: center;
    color: var(--white);
  }
  .card--back .brand__dot { background: var(--white); width: 50px; height: 50px; }
  .card--back .brand__name { color: var(--white); font-size: 30px; }
  .card--back .brand { width: auto; }
  .back__url {
    margin-top: 38px; font-size: 12px; letter-spacing: 4px;
  }
</style>
</head>
<body>
<main class="sheet">
  <section class="card card--front">
    <div class="brand">
      <span class="brand__dot"></span>
      <span class="brand__name">Tranquilly</span>
    </div>
    <span class="divider"></span>
    <div class="details">
      <p class="details__name">Elena Marsh, FNP-C</p>
      <p class="details__role">Co-founder</p>
      <p class="details__address">482 Lantern Avenue, Suite 210,<br>Boulder, CO, United States, Colorado</p>
      <ul class="contact">
        <li class="contact__item">
          <span class="contact__icon"><svg width="8" height="8" viewBox="0 0 24 24"><path fill="#fff" d="M6.6 10.8a15 15 0 0 0 6.6 6.6l2.2-2.2c.3-.3.7-.4 1-.2 1.1.4 2.3.6 3.6.6.6 0 1 .4 1 1V20c0 .6-.4 1-1 1A17 17 0 0 1 3 4c0-.6.4-1 1-1h3.5c.6 0 1 .4 1 1 0 1.3.2 2.5.6 3.6.1.3 0 .7-.2 1z"/></svg></span>
          +1 800-555-0142
        </li>
        <li class="contact__item">
          <span class="contact__icon"><svg width="8" height="8" viewBox="0 0 24 24"><path fill="none" stroke="#fff" stroke-width="2.5" d="M3 6h18v12H3zM3 6l9 7 9-7"/></svg></span>
          hello@tranquillyrestore.com
        </li>
        <li class="contact__item">
          <span class="contact__icon"><svg width="9" height="9" viewBox="0 0 24 24"><g fill="none" stroke="#fff" stroke-width="2"><circle cx="12" cy="12" r="9"/><path d="M3 12h18M12 3c3 3 3 15 0 18M12 3c-3 3-3 15 0 18"/></g></svg></span>
          www.tranquillyrestore.com
        </li>
      </ul>
    </div>
  </section>

  <section class="card card--back">
    <div class="brand">
      <span class="brand__dot"></span>
      <span class="brand__name">Tranquilly</span>
    </div>
    <p class="back__url">www.tranquillyrestore.com</p>
  </section>
</main>
</body>
</html>
```